Modernes Karten-Design für Finanzdienstleister
Zielgruppe
Wir sind ein Finanzdienstleister, der zum einen Teil auf Provisionsbasis und zum anderen Teil auf Honorarbasis arbeitet. Hierfür haben wir auch getrennte Firmenbereiche. Unser Kundenklientel sind Privatpersonen im Alter zwischen 35 und 80 Jahren. Unsere Dienstleistungen drehen sich um alle Versicherungen, aber auch um Geldanlagen, Verfügungen, Vollmachten und Testamente
Aufgabenstellung
Wir benötigen eine Karte, die wir an Kunden verschicken, wenn wir Unterlagen verschicken. Die Karte, die wir bisher haben finden Sie bei den Dateien, die wir hochgeladen haben. Wir möchten nun eine moderne Karte haben mit der wir uns bei unseren Kunden bedanken. Auf der Rückseite der Karte soll wie bisher Platz sein für einen handschriftlichen Gruß von uns oder für sonstige handschriftliche Vermerke. Beim Format der Karte sind wir fexibel. Es müssen unsere Firmenfarben und unser Slogan verwendet werden. Wir möchten ein schnörkelloses modernes Design haben. Bei den hochgeladenen Unterlagen befinden sich auch Vorschläge, die ein Mitarbeiter bereits entworfen hat. Diese gefallen uns aber nicht. Die Webadresse unserer Webseite lautet: https://lindmayr-horizonte.de/
Auf der Rückseite sollen natürlich auch die Adress- und Kontaktdaten mit drauf sein. Wir brauchen hier keine eigenen Bilder und auch kein Stockmaterial. Die Karte soll einfach, schlicht aber stylisch modern sein.

```html
<!DOCTYPE html>
<html lang="de">
<head>
<meta charset="utf-8">
<title>Dankeskarte – Lindmayr Horizonte</title>
<link rel="stylesheet" href="https://fonts.googleapis.com/css2?family=Poppins:wght@500;600;700&display=swap">
<style>
  :root {
    --brand-orange: #e3711a;
    --card-white: #ffffff;
    --ink-dark: #231f20;
    --stage: #ececec;
  }
  * { margin: 0; padding: 0; box-sizing: border-box; }
  html, body { width: 1200px; height: 2620px; overflow: hidden; }
  body {
    background: var(--stage);
    position: relative;
    font-family: "Poppins", sans-serif;
  }
  .card {
    position: absolute;
    left: 214px;
    width: 773px;
    height: 547px;
  }
  .card--front { top: 213px; background: var(--brand-orange); }
  .card--back-a { top: 1024px; background: var(--card-white); }
  .card--back-b { top: 1860px; background: var(--card-white); }

  .front-title {
    position: absolute;
    top: 58px; left: 0; width: 100%;
    text-align: center;
    color: var(--card-white);
    font-weight: 700;
    font-size: 80px;
    letter-spacing: 1px;
  }
  .signature-rule {
    position: absolute;
    left: 226px; top: 451px;
    width: 320px; height: 8px;
    background: var(--card-white);
  }

  .divider {
    position: absolute;
    height: 4px;
    background: var(--brand-orange);
  }
  .card--back-a .divider { left: 45px; width: 682px; top: 381px; }
  .card--back-b .divider { left: 66px; width: 640px; top: 426px; }

  .contact {
    position: absolute;
    color: var(--brand-orange);
    font-weight: 600;
    font-size: 17px;
    line-height: 23px;
    list-style: none;
    white-space: nowrap;
  }
  .card--back-a .contact { left: 60px; top: 416px; }
  .card--back-b .contact--address { left: 91px; top: 465px; }
  .card--back-b .contact--web { left: 414px; top: 465px; }

  .brand {
    position: absolute;
    text-align: center;
    white-space: nowrap;
  }
  .brand-name {
    display: block;
    color: var(--brand-orange);
    font-weight: 500;
    font-size: 33px;
    line-height: 40px;
  }
  .brand-slogan {
    display: block;
    color: var(--ink-dark);
    font-weight: 500;
    font-size: 16px;
    line-height: 22px;
  }
  .card--back-a .brand { left: 380px; width: 340px; top: 430px; }
  .card--back-b .brand { left: 216px; width: 340px; top: 48px; }
</style>
</head>
<body>
  <section class="card card--front">
    <h1 class="front-title">Dankeschön</h1>
    <div class="signature-rule"></div>
  </section>

  <section class="card card--back-a">
    <div class="divider"></div>
    <ul class="contact">
      <li>Kastanienweg 12 • 79098 Freiburg</li>
      <li>Telefon : 0761/48 27 93-10</li>
      <li>info@lindmayr-horizonte.de</li>
      <li>www.lindmayr-horizonte.de</li>
    </ul>
    <div class="brand">
      <span class="brand-name">lindmayr horizonte</span>
      <span class="brand-slogan">Weiter voraus planen.</span>
    </div>
  </section>

  <section class="card card--back-b">
    <div class="brand">
      <span class="brand-name">lindmayr horizonte</span>
      <span class="brand-slogan">Weiter voraus planen.</span>
    </div>
    <div class="divider"></div>
    <ul class="contact contact--address">
      <li>Kastanienweg 12 • 79098 Freiburg</li>
      <li>Telefon : 0761/48 27 93-10</li>
    </ul>
    <ul class="contact contact--web">
      <li>info@lindmayr-horizonte.de</li>
      <li>www.lindmayr-horizonte.de</li>
    </ul>
  </section>
</body>
</html>
```